Company Letter head for formal business correspondence

Company needs a new facelift for stationary. Our letter head is impact as a professional service provider. We need to reflect professionalism in the Safety and Health environment. we work in the whole of the asia pacific region with our main base in Australia Queensland. We are a service company with consulting and operational focus. I have supplied our current logo. I have attached also our first letterhead that we didn't use, Wrong address on it also as we have moved since

Reason: Extension for design review due to modification with some designs currently and Xmas break issue.

Target Market(s)

New clients, government and global companys

Industry/Entity Type

Business

Font styles to use
Sans Serif

Requirements
Must have
• Logo, address, be in word format so l can use as a template and not just printed paper that l place in a printer.
• 14 Varley St, Gladstone, Queensland 4680.
• 1300482716 info@velmorisk.com
Nice to have
• a water mark in the back ground of the logo or partial log as one example supplied

```html
<!DOCTYPE html>
<html lang="en">
<head>
<meta charset="utf-8">
<title>Velmo Risk Letterhead</title>
<link href="https://fonts.googleapis.com/css2?family=Roboto+Slab:wght@300;400;700&display=swap" rel="stylesheet">
<style>
  :root {
    --ink: #222222;
    --text: #3a3a3a;
    --brand-red: #9b1c20;
    --band-dark: #231f20;
    --divider: #8a8a8a;
    --paper: #ffffff;
    --watermark: #ececec;
  }
  * { margin: 0; padding: 0; box-sizing: border-box; }
  html, body { width: 960px; height: 1200px; overflow: hidden; background: var(--paper); }
  .letterhead {
    position: relative;
    width: 960px;
    height: 1200px;
    background: var(--paper);
    font-family: "Roboto Slab", serif;
    color: var(--text);
  }
  .brand {
    position: absolute;
    left: 34px;
    top: 52px;
    display: flex;
    align-items: center;
    gap: 12px;
  }
  .brand-dot {
    width: 34px; height: 34px;
    border-radius: 50%;
    background: var(--brand-red);
  }
  .brand-name {
    font-size: 46px;
    font-weight: 700;
    color: var(--ink);
    letter-spacing: -0.5px;
    line-height: 1;
  }
  .watermark {
    position: absolute;
    right: 32px;
    top: 40px;
    width: 80px; height: 80px;
    border-radius: 50%;
    background: var(--watermark);
    opacity: 0.8;
  }
  .contact-bar {
    position: absolute;
    left: 0; right: 0;
    top: 1102px;
    height: 60px;
    font-size: 18px;
    font-weight: 300;
    color: var(--text);
  }
  .contact-item {
    position: absolute;
    display: flex;
    align-items: center;
    white-space: nowrap;
  }
  .contact-item svg { fill: var(--brand-red); flex: none; }
  .contact-address { left: 22px; top: 6px; align-items: flex-start; }
  .contact-address svg { margin-top: 3px; margin-right: 9px; }
  .contact-address p { line-height: 26px; }
  .contact-phone { left: 454px; top: 18px; }
  .contact-phone svg { margin-right: 9px; }
  .contact-email { left: 702px; top: 18px; font-weight: 400; color: var(--ink); }
  .contact-email svg { margin-right: 12px; }
  .divider {
    position: absolute;
    top: 2px;
    width: 1px;
    height: 46px;
    background: var(--divider);
  }
  .divider-one { left: 391px; }
  .divider-two { left: 640px; }
  .footer-band {
    position: absolute;
    left: 0; bottom: 0;
    width: 960px; height: 21px;
  }
  .band-red { fill: var(--brand-red); }
  .band-dark { fill: var(--band-dark); }
</style>
</head>
<body>
<main class="letterhead">
  <header class="brand">
    <span class="brand-dot"></span>
    <span class="brand-name">Velmo Risk</span>
  </header>
  <div class="watermark" aria-hidden="true"></div>

  <footer class="contact-bar">
    <div class="contact-item contact-address">
      <svg width="20" height="18" viewBox="0 0 20 18" aria-hidden="true">
        <path d="M10 0 L20 9 L17 9 L17 18 L12 18 L12 12 L8 12 L8 18 L3 18 L3 9 L0 9 Z"/>
      </svg>
      <p>14 Varley St.<br>Gladstone, Queensland 4680</p>
    </div>
    <span class="divider divider-one"></span>
    <div class="contact-item contact-phone">
      <svg width="20" height="20" viewBox="0 0 20 20" aria-hidden="true">
        <circle cx="10" cy="10" r="9" fill="none" stroke="#9b1c20" stroke-width="1.6"/>
        <path d="M11.8 4.5 L13.6 5.6 L12.4 8 L11 7.4 C9.8 9 9.2 10.6 9 12.4 L10.4 12.8 L10 15.4 L7.9 15.6 C6.9 11.6 8.6 7 11.8 4.5 Z"/>
      </svg>
      <span>1300 482 716</span>
    </div>
    <span class="divider divider-two"></span>
    <div class="contact-item contact-email">
      <svg width="20" height="14" viewBox="0 0 20 14" aria-hidden="true">
        <path d="M0 0 H20 V2 L10 8 L0 2 Z"/>
        <path d="M0 4 L10 10 L20 4 V14 H0 Z"/>
      </svg>
      <span>info@velmorisk.com</span>
    </div>
  </footer>

  <svg class="footer-band" viewBox="0 0 960 21" aria-hidden="true">
    <polygon class="band-red" points="0,0 442,0 411,21 0,21"/>
    <polygon class="band-dark" points="462,0 960,0 960,21 432,21"/>
  </svg>
</main>
</body>
</html>
```